Bi-Lingual Trash and Recycle Sign

Hello,

Pretty straight forward. I have not been able to find the exact sign we need for a property with trash and recycle guidelines. I've found close, but not complete. We are looking to have metal 12x18 street sign type signs made to provide these instructions. Attached is a sample taken from the web. I want to be sure to avoid conflicting with them so looking for the same wording but in our own. I'd also like to include our company logo, also attached in vector in horizontal and vertical for inclusion.

```html
<!DOCTYPE html>
<html lang="en">
<head>
<meta charset="utf-8">
<title>Recycle / Reciclar Sign</title>
<link rel="stylesheet" href="https://fonts.googleapis.com/css2?family=Montserrat:wght@600;700;800;900&display=swap">
<style>
  :root {
    --metal-light: #f4f5f6;
    --metal-mid: #c9ccd0;
    --metal-dark: #9ea3a8;
    --panel: #ffffff;
    --green-dark: #0b5f3a;
    --green: #17824f;
    --green-light: #e3f1e7;
    --green-icon: #2e9a4c;
    --red: #e3241b;
    --ink: #141414;
    --brand: #3b2a2a;
  }
  * { box-sizing: border-box; margin: 0; padding: 0; }
  html, body { width: 839px; height: 1200px; overflow: hidden; background: #ffffff; }
  body { font-family: "Montserrat", Arial, sans-serif; }

  .sign {
    position: relative;
    width: 839px; height: 1200px;
    border-radius: 26px;
    background: linear-gradient(135deg, var(--metal-light) 0%, var(--metal-mid) 35%, var(--metal-light) 55%, var(--metal-dark) 100%);
    padding: 26px;
  }
  .panel {
    width: 100%; height: 100%;
    background: var(--panel);
    border-radius: 14px;
    overflow: hidden;
    display: flex; flex-direction: column; align-items: center;
  }

  .header {
    width: 100%;
    height: 200px;
    background: linear-gradient(180deg, var(--green-dark) 0%, var(--green) 100%);
    color: #fff;
    display: flex; flex-direction: column; align-items: center; justify-content: center;
    font-weight: 800;
    font-size: 78px;
    line-height: 1;
    letter-spacing: 1px;
  }
  .header .rule { width: 480px; height: 5px; background: #fff; margin: 12px 0 10px; }

  .no-bags-icon { margin-top: 22px; width: 72px; height: 72px; }

  .warning {
    color: var(--red);
    font-weight: 800;
    font-size: 33px;
    line-height: 1.12;
    text-align: center;
    margin-top: 14px;
  }

  .recycle-icon { margin-top: 26px; width: 66px; height: 66px; }

  .stream {
    font-weight: 800;
    font-size: 27px;
    line-height: 1.2;
    color: var(--ink);
    text-align: center;
    margin-top: 16px;
  }

  .accepted {
    width: 628px;
    margin-top: 22px;
    border: 4px solid var(--green);
    border-radius: 14px;
    background: var(--green-light);
    overflow: hidden;
  }
  .accepted-title {
    background: var(--green);
    color: #fff;
    font-weight: 800;
    font-size: 27px;
    text-align: center;
    padding: 12px 0 10px;
  }
  .accepted-list { list-style: none; padding: 14px 26px 16px; }
  .accepted-list li {
    font-weight: 700;
    font-size: 20px;
    line-height: 1.35;
    color: var(--ink);
    padding-left: 22px;
    position: relative;
    margin-bottom: 6px;
  }
  .accepted-list li::before {
    content: "";
    position: absolute; left: 0; top: 7px;
    width: 11px; height: 11px;
    background: var(--green);
  }

  .no-trash { margin-top: 26px; }

  .brand {
    margin-top: 30px;
    display: flex; align-items: center; gap: 14px;
    color: var(--brand);
    font-weight: 800;
    font-size: 34px;
    letter-spacing: 2px;
    text-transform: uppercase;
    line-height: 1.1;
  }
  .brand-mark { width: 36px; height: 36px; background: var(--brand); flex: none; }
</style>
</head>
<body>
  <div class="sign">
    <div class="panel">
      <header class="header">
        <span>RECYCLE</span>
        <span class="rule"></span>
        <span>RECICLAR</span>
      </header>

      <svg class="no-bags-icon" viewBox="0 0 72 72" aria-hidden="true">
        <path d="M24 24 L48 24 L50 54 L22 54 Z" fill="#141414"/>
        <path d="M26 24 Q27 14 31 24 M41 24 Q45 14 46 24" fill="none" stroke="#141414" stroke-width="3"/>
        <circle cx="36" cy="36" r="32" fill="none" stroke="#e3241b" stroke-width="6"/>
        <line x1="14" y1="14" x2="58" y2="58" stroke="#e3241b" stroke-width="6"/>
      </svg>

      <p class="warning">NO PLASTIC BAGS / NO SE ACEPTAN<br>BOLSAS PLÁSTICAS</p>

      <svg class="recycle-icon" viewBox="0 0 66 66" aria-hidden="true">
        <g fill="none" stroke="#2e9a4c" stroke-width="7" stroke-linejoin="round">
          <path d="M27 10 L39 10 L48 26"/>
          <path d="M56 38 L50 50 L32 50"/>
          <path d="M20 50 L10 50 L18 33"/>
        </g>
        <g fill="#2e9a4c">
          <path d="M41 24 L55 22 L50 35 Z"/>
          <path d="M34 42 L26 52 L36 58 Z"/>
          <path d="M12 30 L24 26 L22 40 Z"/>
        </g>
      </svg>

      <p class="stream">Single-Stream Recycling /<br>Reciclaje de Flujo Único</p>

      <section class="accepted">
        <h2 class="accepted-title">Accepted Items / Materiales Aceptados:</h2>
        <ul class="accepted-list">
          <li>Glass, Tin, Aluminum / Vidrio, Hojalata, Aluminio</li>
          <li>Plastics (#1–7) / Plásticos (#1–7)</li>
          <li>Cardboard / Cartón</li>
          <li>Mixed Paper, Newspapers, Magazines / Papel Mixto, Periódicos, Revistas</li>
        </ul>
      </section>

      <p class="warning no-trash">DO NOT INCLUDE TRASH /<br>NO INCLUIR BASURA</p>

      <div class="brand">
        <span class="brand-mark"></span>
        <span>Briarwood<br>Management</span>
      </div>
    </div>
  </div>
</body>
</html>
```